KTRWG Promotion Flyer to raise money and communicate our goals

We need a flyer that promotes our organization. We are a 501(c)3 trying to raise money for Arts, Education and Entrepreneurship in our small town.

We promote a social events that improve qualtiy of life and educate people on how to start and expand businesses. Our goal is to make downtown an active and thriving place with many things for people to do and enjoy as well as create a favorable place for business.

Target Market(s)

Wealthy donors and Organizations with cash

Industry/Entity Type

Education

Colors

Designer to choose colors to be used in the design.

Requirements
Must have
• Eye catching graphics and look very professional
• Should appeal to men and women
Nice to have
• Make use of any known psychological colors and fonts etc... that appeal to philanthropic people
Should not have
• Should not be complicated or confusing

```html
<!DOCTYPE html>
<html lang="en">
<head>
<meta charset="utf-8">
<title>KTRWG Flyer</title>
<link href="https://fonts.googleapis.com/css2?family=Open+Sans:wght@400;600&family=Arimo&display=swap" rel="stylesheet">
<style>
  :root {
    --blue-deep: #1c4f95;
    --blue-mid: #2f6db5;
    --blue-light: #7fb0e2;
    --grey: #b9bcc0;
    --ink: #2b2b2b;
    --paper: #ffffff;
  }
  * { margin: 0; padding: 0; box-sizing: border-box; }
  html, body { width: 971px; height: 1200px; overflow: hidden; background: var(--paper); }
  .flyer { position: relative; width: 971px; height: 1200px; font-family: "Open Sans", sans-serif; color: var(--ink); }
  .flyer-graphics { position: absolute; inset: 0; }
  .brand { position: absolute; right: 70px; top: 36px; text-align: center; }
  .brand-row { display: flex; align-items: center; justify-content: center; gap: 10px; }
  .brand-mark { width: 28px; height: 28px; background: var(--blue-mid); }
  .brand-name { font-size: 32px; font-weight: 600; color: var(--blue-deep); letter-spacing: 1px; }
  .brand-tagline { font-size: 9px; color: var(--ink); letter-spacing: 1px; text-transform: uppercase; margin-top: 2px; }
  .intro { position: absolute; left: 46px; top: 706px; width: 566px; font-size: 12.5px; line-height: 16.2px; }
  .intro p { margin-bottom: 5px; }
  .intro .lead { margin-bottom: 11px; }
  .intro .appeal { margin-top: 14px; margin-bottom: 0; text-align: justify; }
  .side-photo { position: absolute; left: 680px; top: 759px; width: 255px; height: 358px;
    background: linear-gradient(180deg, #dfe7ef 0%, #d4dde6 10%, #7a2e30 22%, #6e2a2c 60%, #9a9470 80%, #b3a77c 100%); }
  .footer { position: absolute; left: 0; right: 0; bottom: 0; height: 56px;
    background: linear-gradient(90deg, var(--blue-deep) 0%, var(--blue-mid) 45%, var(--blue-light) 75%, var(--blue-mid) 100%);
    display: flex; align-items: center; justify-content: space-between; padding: 0 25px 0 40px; color: #fff; }
  .footer-web { display: flex; align-items: center; gap: 12px; font-size: 20px; }
  .footer-call { font-family: "Arimo", sans-serif; font-size: 34px; }
</style>
</head>
<body>
<div class="flyer">
  <svg class="flyer-graphics" width="971" height="1200" viewBox="0 0 971 1200">
    <defs>
      <linearGradient id="sceneTone" x1="0" y1="0" x2="0" y2="1">
        <stop offset="0" stop-color="#6ea6dc"/>
        <stop offset="0.4" stop-color="#b9d6ef"/>
        <stop offset="0.55" stop-color="#b8866b"/>
        <stop offset="0.78" stop-color="#8d7f5a"/>
        <stop offset="1" stop-color="#6f7d45"/>
      </linearGradient>
      <linearGradient id="swooshBlue" x1="0" y1="0" x2="1" y2="0">
        <stop offset="0" stop-color="#2c5fa6"/>
        <stop offset="0.6" stop-color="#1c4f95"/>
        <stop offset="1" stop-color="#5d93cf"/>
      </linearGradient>
      <radialGradient id="forestTone" cx="0.5" cy="0.4" r="0.6">
        <stop offset="0" stop-color="#e8e3a8"/>
        <stop offset="0.5" stop-color="#8b8a55"/>
        <stop offset="1" stop-color="#4f6a2a"/>
      </radialGradient>
    </defs>
    <path role="img" aria-label="Photo of the covered town pavilion with a red roof under a blue sky"
      d="M0,130 C320,100 550,250 750,275 C820,285 900,280 971,245 L971,625 C940,650 880,680 800,690 C620,712 420,660 280,575 C200,545 100,540 0,540 Z" fill="url(#sceneTone)"/>
    <path d="M0,108 C320,88 450,140 530,195 C400,140 250,118 0,142 Z" fill="var(--grey)"/>
    <path d="M0,75 C250,40 550,200 800,228 C880,238 940,212 971,190 L971,250 C900,285 820,290 750,280 C550,250 320,88 0,110 Z" fill="url(#swooshBlue)"/>
    <path d="M280,575 C420,660 620,712 800,690 C880,680 940,650 971,625 L971,688 C930,708 870,716 800,716 C620,714 430,662 280,575 Z" fill="url(#swooshBlue)"/>
    <circle cx="153" cy="581" r="108" fill="var(--grey)"/>
    <circle role="img" aria-label="Photo of a sunlit pine forest" cx="153" cy="581" r="98" fill="url(#forestTone)"/>
  </svg>

  <div class="brand">
    <div class="brand-row"><span class="brand-mark"></span><span class="brand-name">KTRWG</span></div>
    <div class="brand-tagline">Cedar Hollow Small Business Association</div>
  </div>

  <div class="intro">
    <p class="lead">The Cedar Hollow Small Business Association (KTRWG) is a local leader in the areas of Arts, Education and Entrepreneurship and is working diligently to promote Cedar Hollow and revitalize our downtown. When you become an KTRWG Member, you will be a part of the citywide work that the KTRWG does every day to improve the lives of citizens of Cedar Hollow:</p>
    <p>We promote Cedar Hollow Hotels, Shopping and Events that make Cedar Hollow a pleasant, exciting and prosperous place to live.</p>
    <p>We provide training and resources to anyone interested Arts, Education and Entrepreneurship.</p>
    <p>We help entrepreneur's start and grow their businesses in a tax efficient and appropriate way.</p>
    <p>We work with all levels of local government to promote our community and create a fertile environment for growth.</p>
    <p class="appeal">Every day, we look for ways to help our local businesses grow and expand, but we need you by our side. As an KTRWG Member, you can help provide training, education and support, and you can give our many businesses a chance to grow and our citizens the opportunity to experience big town amenities and events in a small town. Members' regular monthly gifts provide a consistent, reliable income stream that allows us to spend less time fundraising—and more time helping our businesses and community. Becoming an KTRWG Member is an easy, efficient and tax-deductible way to make a difference for our community all year long. Please donate today.</p>
  </div>

  <div class="side-photo" role="img" aria-label="Photo of the town welcome sign at the trail head park showing a holiday greeting"></div>

  <div class="footer">
    <div class="footer-web">
      <svg width="18" height="18" viewBox="0 0 18 18" fill="none" stroke="#fff" stroke-width="1.5">
        <circle cx="9" cy="9" r="7.5"/><ellipse cx="9" cy="9" rx="3.2" ry="7.5"/><line x1="1.5" y1="9" x2="16.5" y2="9"/>
      </svg>
      <span>www.website.com</span>
    </div>
    <div class="footer-call">CALL US:1234-456-789</div>
  </div>
</div>
</body>
</html>
```